Lumen Thread Business Card Design

Lumen Thread is a platform that allows advertisers and their agencies to build media plans across millions of influencers that support their objectives. Once the media plan is approved, it allows you collaborate with influencers, approve creative direction and distribute content across over 20 channels, all while ensuring it is measured and in line with your guidelines.

We are looking for a designer to help us create one of the most unique business cards you have ever received. In summary, we are looking for one side of our business card design to incorporate our logo and contact details and the second side to incorporate what we do, show different social media images.

Size : See attachment for size guidelines. Square Business Card Template.

Logo : See attached.

Front :
Logo : Lumen Thread (attached)
Name: Marisol Bekker
Job Title: Co - Founder
Phone Number : Au +61 400 583 917
Email : marisol.bekker@lumenthread.com
Web : lumenthread.com

Back :
We would like to see 3 versions for the back.

Back One
Pictora Picture : See attached Full Size Render 5
lumen thread Logo : Somehow watermarked over the picture in a subtle way
Copy : Pictora Logo @marisolbek8 / Genre - Fashion

Back Two
Kinbridge Picture : See attached Full Size Render 4
Copy : Kinbridge Logo @marisolbek8 / Genre - Travel

Back Three
Chirpline Copy : "Toasting to exciting adventures in my gorgeous new dress and dancing shoes. Here’s to a glitzy and dazzling 2015!"
Copy : Chirpline Logo @marisolbek8 / Genre - Business

Note : Social Media Logos attached

Target Market(s)

See Project Description

Industry/Entity Type

Business

Contact Information for Business Card

See Project Description

Font styles to use
Other font styles liked:
• See Logo

Colors
1696d0
33a6d7
85cae6
0355a3
ec1f27

Requirements
Must have
• See Project Description
Nice to have
• See Project Description
Should not have
• See Project Description

```html
<!DOCTYPE html>
<html lang="en">
<head>
<meta charset="utf-8">
<title>Lumen Thread – Business Cards</title>
<link rel="stylesheet" href="https://fonts.googleapis.com/css2?family=Open+Sans:wght@400;600;700&display=swap">
<style>
  :root {
    --page-bg: #ececec;
    --card-blue: #85cae6;
    --brand-blue: #1696d0;
    --mid-blue: #33a6d7;
    --deep-blue: #0355a3;
    --white: #ffffff;
    --pictora-purple: #6a3d98;
    --kinbridge-blue: #3b6fb6;
    --chirpline-blue: #2a86c8;
  }
  * { box-sizing: border-box; margin: 0; padding: 0; }
  html, body {
    width: 1200px; height: 1200px; overflow: hidden;
    background: var(--page-bg);
    font-family: "Open Sans", Arial, sans-serif;
  }
  .sheet { position: relative; width: 1200px; height: 1200px; }

  .card {
    position: absolute;
    width: 370px; height: 370px;
    background: var(--card-blue);
    overflow: hidden;
  }

  /* Front */
  .card--front { left: 150px; top: 170px; }
  .brand {
    position: absolute; left: 48px; top: 62px;
    display: flex; align-items: center; gap: 12px;
  }
  .brand__mark {
    width: 50px; height: 50px; background: var(--deep-blue); border-radius: 6px;
  }
  .brand__name {
    font-size: 40px; font-weight: 700; color: var(--brand-blue);
    line-height: 1; letter-spacing: -0.5px;
  }
  .person { position: absolute; left: 0; right: 0; top: 162px; text-align: center; }
  .person__name { font-size: 24px; font-weight: 700; color: var(--white); }
  .person__role { font-size: 17px; font-weight: 700; color: var(--deep-blue); margin-top: 8px; }
  .contact {
    position: absolute; left: 40px; top: 262px;
    list-style: none; font-size: 14px; color: var(--deep-blue);
  }
  .contact__item { display: flex; align-items: center; gap: 8px; line-height: 24px; }
  .contact__icon { width: 16px; height: 16px; flex: none; }

  /* Social backs */
  .card--pictora { left: 680px; top: 140px; }
  .card--kinbridge { left: 680px; top: 625px; }
  .card--chirpline { left: 150px; top: 720px; }

  .photo { position: absolute; left: 0; top: 0; width: 100%; height: 300px; }
  .photo--fashion { background: linear-gradient(160deg, #c8687c 0%, #d98a97 55%, #b9566b 100%); }
  .photo--travel { background: linear-gradient(180deg, #9cbbd6 0%, #cbd4d6 45%, #6b6a64 70%, #2c2a27 100%); }

  .tagline {
    position: absolute; left: 0; right: 0; bottom: 0; height: 70px;
    display: flex; align-items: center; gap: 10px; padding-left: 18px;
    color: var(--white); font-size: 15px; font-weight: 700;
  }
  .card--chirpline .tagline { height: 76px; }
  .tagline__dot { width: 40px; height: 40px; border-radius: 50%; flex: none; }
  .tagline__dot--pictora { background: var(--pictora-purple); }
  .tagline__dot--kinbridge { background: var(--kinbridge-blue); }
  .tagline__dot--chirpline { background: var(--chirpline-blue); }

  .bubble { position: absolute; left: 18px; top: 20px; width: 334px; height: 270px; }
  .bubble__text {
    position: absolute; left: 62px; top: 62px; width: 250px;
    text-align: center; color: var(--white);
    font-size: 16px; font-weight: 700; line-height: 1.35;
  }
</style>
</head>
<body>
<main class="sheet">

  <section class="card card--front" aria-label="Front of card">
    <div class="brand">
      <span class="brand__mark"></span>
      <span class="brand__name">lumen thread</span>
    </div>
    <div class="person">
      <p class="person__name">Marisol Bekker</p>
      <p class="person__role">Co - Founder</p>
    </div>
    <ul class="contact">
      <li class="contact__item">
        <svg class="contact__icon" viewBox="0 0 16 16"><path d="M4 2l3 3-1.5 1.5a8 8 0 0 0 4 4L11 9l3 3-2 2C7 14 2 9 2 4z" fill="#ffffff"/></svg>
        Au +61 400 583 917
      </li>
      <li class="contact__item">
        <svg class="contact__icon" viewBox="0 0 16 16"><rect x="1.5" y="3.5" width="13" height="9" fill="none" stroke="#ffffff" stroke-width="1.5"/><path d="M1.5 3.5L8 9l6.5-5.5" fill="none" stroke="#ffffff" stroke-width="1.5"/></svg>
        marisol.bekker@lumenthread.com
      </li>
      <li class="contact__item">
        <svg class="contact__icon" viewBox="0 0 16 16"><text x="8" y="13" text-anchor="middle" font-family="Open Sans, sans-serif" font-size="14" font-weight="700" fill="#ffffff">@</text></svg>
        lumenthread.com
      </li>
    </ul>
  </section>

  <section class="card card--pictora" aria-label="Back – fashion">
    <div class="photo photo--fashion" role="img" aria-label="Fashion photograph of three people posing against a pink backdrop"></div>
    <div class="tagline">
      <span class="tagline__dot tagline__dot--pictora"></span>
      <span>Pictora @marisolbek8 / Genre - Fashion</span>
    </div>
  </section>

  <section class="card card--chirpline" aria-label="Back – business">
    <svg class="bubble" viewBox="0 0 334 270" aria-hidden="true">
      <defs>
        <radialGradient id="bubble-fill" cx="50%" cy="45%" r="60%">
          <stop offset="0" stop-color="#33a6d7"/>
          <stop offset="0.8" stop-color="#1679bd"/>
          <stop offset="1" stop-color="#0355a3"/>
        </radialGradient>
      </defs>
      <path d="M167 8C82 8 22 48 22 106c0 50 44 88 108 96l-20 44 52-42C250 202 312 162 312 106 312 48 252 8 167 8z" fill="url(#bubble-fill)"/>
      <circle cx="88" cy="258" r="8" fill="#0355a3"/>
    </svg>
    <p class="bubble__text">Toasting to exciting adventures in my gorgeous new dress and dancing shoes. Here’s to a glitzy and dazzling 2015!</p>
    <div class="tagline">
      <span class="tagline__dot tagline__dot--chirpline"></span>
      <span>Chirpline @marisolbek8 / Genre - Business</span>
    </div>
  </section>

  <section class="card card--kinbridge" aria-label="Back – travel">
    <div class="photo photo--travel" role="img" aria-label="Travel photograph through an aircraft window of an airport apron at sunset with a raised glass"></div>
    <div class="tagline">
      <span class="tagline__dot tagline__dot--kinbridge"></span>
      <span>Kinbridge @marisolbek8 / Genre - Travel</span>
    </div>
  </section>

</main>
</body>
</html>
```